Summit Shield Coatings Inc facebook rebranding

We had our facebook design done 3 years ago and we need to get it more updated and attractive. I have attached what we already use and here below is a link to our page. i have 2 locations so when we pick a design we will need files to have each locations logo and phone number
location 1- Summit Shield Coatings Inc. 469-555-0148
Location 2- Summit Shield Coatings of west texas inc. 806-555-0192
here is link
Target Market(s)
contractors and homeowners
Industry/Entity Type
Insulation
Font styles to use
Serif
Colors
0054AA
0677BA
7BADD7
CADEEF
E8F1F8

```html
<!DOCTYPE html>
<html lang="en">
<head>
<meta charset="utf-8">
<title>Summit Shield Coatings – Facebook Covers</title>
<link rel="stylesheet" href="https://fonts.googleapis.com/css2?family=Audiowide&family=Poppins:wght@500;600;700&family=Russo+One&family=Montserrat:wght@400&display=swap">
<style>
  :root{
    --sheet:#d6e5ef;
    --navy:#06203f;
    --brand-blue:#0054AA;
    --sky:#1fa6e3;
    --ink:#0d1b2e;
    --white:#ffffff;
    --label:#3d4a56;
  }
  *{box-sizing:border-box;margin:0;padding:0}
  html,body{width:1200px;height:938px;overflow:hidden;background:var(--sheet)}
  .sheet{position:relative;width:1200px;height:938px}
  .cover-label{
    position:absolute;left:66px;transform:translate(-50%,-50%) rotate(-90deg);
    font-family:"Montserrat",sans-serif;font-size:31px;letter-spacing:1px;color:var(--label);white-space:nowrap;
  }
  .cover{
    position:absolute;left:121px;width:1003px;height:371px;overflow:hidden;background:var(--white);
    box-shadow:8px 10px 10px rgba(0,0,0,.45);
  }
  .cover-art{position:absolute;inset:0}
  .brand{position:absolute;left:42px;top:30px;display:flex;align-items:flex-start;gap:9px;white-space:nowrap}
  .brand-mark{width:20px;height:20px;background:var(--brand-blue);flex:none;margin-top:5px}
  .brand-name{font-family:"Poppins",sans-serif;font-weight:700;font-size:20px;line-height:1.2;color:var(--brand-blue)}
  .divider{position:absolute;left:257px;top:20px;width:1px;height:100px;background:#d3d8de}
  .call{position:absolute;left:280px;top:32px}
  .call-head{display:flex;align-items:center;gap:10px;font-family:"Audiowide",sans-serif;font-size:30px;color:var(--navy);letter-spacing:1px}
  .call-number{font-family:"Poppins",sans-serif;font-weight:700;font-size:28px;color:var(--ink);margin-top:0;letter-spacing:1px}
  .location{position:absolute;left:518px;top:36px;display:flex;gap:6px;font-family:"Poppins",sans-serif;font-weight:600;font-size:20px;line-height:1.22;color:var(--ink);white-space:nowrap}
  .location svg{flex:none;margin-top:3px}
  .headline{position:absolute;left:46px;top:150px;font-family:"Russo One",sans-serif;color:var(--white);line-height:1;white-space:nowrap}
  .headline-top{font-size:38px;letter-spacing:5.5px;color:transparent;-webkit-text-stroke:1.4px #cfe6ff;background:linear-gradient(180deg,#5bb8ff,#0a4fa0);-webkit-background-clip:text;background-clip:text}
  .headline-bottom{font-size:38px;letter-spacing:3.5px;margin-top:3px}
  .services-tag{position:absolute;left:239px;top:229px;width:146px;height:25px;border-radius:13px;background:var(--sky);
    font-family:"Russo One",sans-serif;font-size:19px;color:var(--white);text-align:center;line-height:25px;letter-spacing:.5px}
  .service-list{position:absolute;left:238px;top:260px;width:360px;list-style:none;display:grid;grid-template-columns:202px 158px;row-gap:10px;
    font-family:"Poppins",sans-serif;font-weight:600;font-size:15px;color:var(--white)}
  .service-list li{display:flex;align-items:center;gap:8px;height:20px;white-space:nowrap}
  .service-list li.wide{grid-column:1 / span 2}
  .web{position:absolute;left:640px;top:296px;height:44px;display:flex;align-items:center;gap:14px;font-family:"Poppins",sans-serif;font-weight:600;font-size:24px;color:var(--white);letter-spacing:1.5px;white-space:nowrap}
  .web-icon{width:28px;height:28px;border-radius:50%;background:var(--white);display:flex;align-items:center;justify-content:center}
</style>
</head>
<body>
<main class="sheet">

  <span class="cover-label" style="top:259px">FACEBOOK COVER 1</span>
  <span class="cover-label" style="top:679px">FACEBOOK COVER 2</span>

  <!-- Location 2 -->
  <section class="cover" style="top:74px">
    <svg class="cover-art" width="1003" height="371" viewBox="0 0 1003 371">
      <defs>
        <linearGradient id="photoBase1" x1="0" x2="1" y1="0" y2="0">
          <stop offset="0" stop-color="#ffffff" stop-opacity="0"/>
          <stop offset=".22" stop-color="#f2e8d6"/>
          <stop offset=".45" stop-color="#e6d3b2"/>
          <stop offset=".7" stop-color="#efe8da"/>
          <stop offset="1" stop-color="#e3d2b4"/>
        </linearGradient>
        <radialGradient id="photoSuit1" cx="800" cy="250" r="200" gradientUnits="userSpaceOnUse" gradientTransform="translate(800 250) scale(0.85 1.15) translate(-800 -250)">
          <stop offset="0" stop-color="#2455b0"/>
          <stop offset=".55" stop-color="#3566c0" stop-opacity=".8"/>
          <stop offset="1" stop-color="#3566c0" stop-opacity="0"/>
        </radialGradient>
        <linearGradient id="panel1" x1="0" x2="0" y1="0" y2="1">
          <stop offset="0" stop-color="#0d4a8c"/>
          <stop offset="1" stop-color="#030e1f"/>
        </linearGradient>
      </defs>
      <g role="img" aria-label="Photo of an insulation installer in a blue protective suit spraying foam between wall studs">
        <rect x="300" y="0" width="703" height="371" fill="url(#photoBase1)"/>
        <rect x="560" y="40" width="443" height="331" fill="url(#photoSuit1)"/>
      </g>
      <path d="M0 138 H500 Q545 138 565 175 L636 371 H0 Z" fill="#ffffff"/>
      <path d="M0 138 H492 Q532 140 550 175 L622 371 H0 Z" fill="url(#panel1)"/>
      <path d="M612 296 H1003 V340 H627 Z" fill="var(--sky)"/>
      <path d="M612 296 H660 L646 340 H627 Z" fill="var(--navy)"/>
    </svg>

    <div class="brand"><span class="brand-mark"></span><span class="brand-name">Summit Shield<br>Coatings<br>of West Texas Inc</span></div>
    <div class="divider"></div>
    <div class="call">
      <div class="call-head">
        <svg width="34" height="34" viewBox="0 0 34 34"><circle cx="17" cy="17" r="17" fill="var(--navy)"/><path d="M11 9c1.5-1 2.5 0 3.5 2l1 2c.4 1-.2 1.6-1 2.2 1 2 2.3 3.4 4.3 4.4.6-.8 1.2-1.4 2.2-1l2 1c2 1 3 2 2 3.5-1.5 2-3.5 2.4-6 1.2C14.5 22.5 11.4 19.5 9.6 15.3 8.5 12.7 9 10.6 11 9z" fill="var(--sky)"/></svg>
        CALL US
      </div>
      <div class="call-number">806-555-0192</div>
    </div>
    <div class="location">
      <svg width="16" height="20" viewBox="0 0 16 20"><path d="M8 0a7.5 7.5 0 0 1 7.5 7.5C15.5 13 8 20 8 20S.5 13 .5 7.5A7.5 7.5 0 0 1 8 0z" fill="var(--navy)"/><circle cx="8" cy="7.5" r="3" fill="#fff"/></svg>
      <span>Summit Shield Coatings<br>of west texas inc</span>
    </div>
    <div class="headline"><div class="headline-top">PROTECTION</div><div class="headline-bottom">THAT MATTERS</div></div>
    <div class="services-tag">SERVICES</div>
    <ul class="service-list">
      <li class="wide"><svg width="16" height="14" viewBox="0 0 16 14"><path d="M1 7l5 5L15 1" stroke="var(--sky)" stroke-width="2.6" fill="none"/></svg>Spray Foam Insulation</li>
      <li><svg width="16" height="14" viewBox="0 0 16 14"><path d="M1 7l5 5L15 1" stroke="var(--sky)" stroke-width="2.6" fill="none"/></svg>Fiberglass Insulation</li>
      <li><svg width="16" height="14" viewBox="0 0 16 14"><path d="M1 7l5 5L15 1" stroke="var(--sky)" stroke-width="2.6" fill="none"/></svg>Air Sealing</li>
      <li><svg width="16" height="14" viewBox="0 0 16 14"><path d="M1 7l5 5L15 1" stroke="var(--sky)" stroke-width="2.6" fill="none"/></svg>Insulation Removal</li>
      <li><svg width="16" height="14" viewBox="0 0 16 14"><path d="M1 7l5 5L15 1" stroke="var(--sky)" stroke-width="2.6" fill="none"/></svg>Attic Ventilation</li>
    </ul>
    <div class="web">
      <span class="web-icon"><svg width="18" height="18" viewBox="0 0 18 18" fill="none" stroke="var(--navy)" stroke-width="1.3"><circle cx="9" cy="9" r="8"/><ellipse cx="9" cy="9" rx="3.5" ry="8"/><path d="M1 9h16M2.5 5h13M2.5 13h13"/></svg></span>
      westtexasshield.com
    </div>
  </section>

  <!-- Location 1 -->
  <section class="cover" style="top:494px">
    <svg class="cover-art" width="1003" height="371" viewBox="0 0 1003 371">
      <defs>
        <linearGradient id="photoBase2" x1="0" x2="1" y1="0" y2="0">
          <stop offset="0" stop-color="#ffffff" stop-opacity="0"/>
          <stop offset=".22" stop-color="#f2e8d6"/>
          <stop offset=".45" stop-color="#e6d3b2"/>
          <stop offset=".7" stop-color="#efe8da"/>
          <stop offset="1" stop-color="#e3d2b4"/>
        </linearGradient>
        <radialGradient id="photoSuit2" cx="800" cy="250" r="200" gradientUnits="userSpaceOnUse" gradientTransform="translate(800 250) scale(0.85 1.15) translate(-800 -250)">
          <stop offset="0" stop-color="#2455b0"/>
          <stop offset=".55" stop-color="#3566c0" stop-opacity=".8"/>
          <stop offset="1" stop-color="#3566c0" stop-opacity="0"/>
        </radialGradient>
        <linearGradient id="panel2" x1="0" x2="0" y1="0" y2="1">
          <stop offset="0" stop-color="#0d4a8c"/>
          <stop offset="1" stop-color="#030e1f"/>
        </linearGradient>
      </defs>
      <g role="img" aria-label="Photo of an insulation installer in a blue protective suit spraying foam between wall studs">
        <rect x="300" y="0" width="703" height="371" fill="url(#photoBase2)"/>
        <rect x="560" y="40" width="443" height="331" fill="url(#photoSuit2)"/>
      </g>
      <path d="M0 138 H500 Q545 138 565 175 L636 371 H0 Z" fill="#ffffff"/>
      <path d="M0 138 H492 Q532 140 550 175 L622 371 H0 Z" fill="url(#panel2)"/>
      <path d="M612 296 H1003 V340 H627 Z" fill="var(--sky)"/>
      <path d="M612 296 H660 L646 340 H627 Z" fill="var(--navy)"/>
    </svg>

    <div class="brand"><span class="brand-mark"></span><span class="brand-name">Summit Shield<br>Coatings Inc</span></div>
    <div class="divider"></div>
    <div class="call">
      <div class="call-head">
        <svg width="34" height="34" viewBox="0 0 34 34"><circle cx="17" cy="17" r="17" fill="var(--navy)"/><path d="M11 9c1.5-1 2.5 0 3.5 2l1 2c.4 1-.2 1.6-1 2.2 1 2 2.3 3.4 4.3 4.4.6-.8 1.2-1.4 2.2-1l2 1c2 1 3 2 2 3.5-1.5 2-3.5 2.4-6 1.2C14.5 22.5 11.4 19.5 9.6 15.3 8.5 12.7 9 10.6 11 9z" fill="var(--sky)"/></svg>
        CALL US
      </div>
      <div class="call-number" style="font-size:29px">469-555-0148</div>
    </div>
    <div class="location">
      <svg width="16" height="20" viewBox="0 0 16 20"><path d="M8 0a7.5 7.5 0 0 1 7.5 7.5C15.5 13 8 20 8 20S.5 13 .5 7.5A7.5 7.5 0 0 1 8 0z" fill="var(--navy)"/><circle cx="8" cy="7.5" r="3" fill="#fff"/></svg>
      <span>Summit Shield Coatings inc</span>
    </div>
    <div class="headline"><div class="headline-top">PROTECTION</div><div class="headline-bottom">THAT MATTERS</div></div>
    <div class="services-tag">SERVICES</div>
    <ul class="service-list">
      <li class="wide"><svg width="16" height="14" viewBox="0 0 16 14"><path d="M1 7l5 5L15 1" stroke="var(--sky)" stroke-width="2.6" fill="none"/></svg>Spray Foam Insulation</li>
      <li><svg width="16" height="14" viewBox="0 0 16 14"><path d="M1 7l5 5L15 1" stroke="var(--sky)" stroke-width="2.6" fill="none"/></svg>Fiberglass Insulation</li>
      <li><svg width="16" height="14" viewBox="0 0 16 14"><path d="M1 7l5 5L15 1" stroke="var(--sky)" stroke-width="2.6" fill="none"/></svg>Air Sealing</li>
      <li><svg width="16" height="14" viewBox="0 0 16 14"><path d="M1 7l5 5L15 1" stroke="var(--sky)" stroke-width="2.6" fill="none"/></svg>Insulation Removal</li>
      <li><svg width="16" height="14" viewBox="0 0 16 14"><path d="M1 7l5 5L15 1" stroke="var(--sky)" stroke-width="2.6" fill="none"/></svg>Attic Ventilation</li>
    </ul>
    <div class="web" style="font-size:21px;letter-spacing:.3px">
      <span class="web-icon"><svg width="18" height="18" viewBox="0 0 18 18" fill="none" stroke="var(--navy)" stroke-width="1.3"><circle cx="9" cy="9" r="8"/><ellipse cx="9" cy="9" rx="3.5" ry="8"/><path d="M1 9h16M2.5 5h13M2.5 13h13"/></svg></span>
      summitshieldcoatings.com
    </div>
  </section>

</main>
</body>
</html>
```